Business card for a vending machine business

I need a business card for my vending machine business. The name is Brightwell Snacks, LLC. The card is one-sided, and landscape format. Not portrait.

The information for the card is as follows:

Dora Quinlan
Owner
(555) 314-2096
Brightwellsnacks.example
Info@brightwellsnacks.example

I'd like colors and design elements to match what's in my logo and company name. I'd like to have the checkered flag or racing stripe if possible You can use a border if youd like. You can use a background color if it looks nice and doesn't clash with the logo
Use your creativity. But a white background is perfectly fine. The card can be as simple, yet gets the point across to match the company name and logo.

I uploaded a copy of my logo. I also uploaded a businesses card I started to create, but since it was missing something, I gave up. Another upload has a red thunderbolt and the checkerer flag. Those two uploads are for inspiration. Again, please make sure to make the card landscape, not portrait. Thank you, designers. Good luck to all.

```html
<!DOCTYPE html>
<html lang="en">
<head>
<meta charset="utf-8">
<title>Brightwell Snacks, LLC – Business Card</title>
<link rel="stylesheet" href="https://fonts.googleapis.com/css2?family=Poppins:wght@300;400;700&display=swap">
<style>
  :root {
    --navy: #1b2d63;
    --navy-deep: #15224d;
    --navy-light: #24397a;
    --red: #e3101f;
    --white: #ffffff;
    --paper: #f7f6fa;
    --ink: #1b2d63;
    --stage: #e9e9ee;
  }
  * { margin: 0; padding: 0; box-sizing: border-box; }
  html, body {
    width: 1200px;
    height: 789px;
    overflow: hidden;
    background: var(--stage);
    font-family: "Poppins", Arial, sans-serif;
  }
  .canvas {
    position: relative;
    width: 1200px;
    height: 789px;
    display: flex;
    align-items: center;
    justify-content: center;
    gap: 40px;
  }
  .card {
    position: relative;
    width: 540px;
    height: 309px;
    border-radius: 22px;
    overflow: hidden;
    box-shadow: 0 6px 18px rgba(20, 25, 60, 0.18);
  }

  /* Front side */
  .card-front { background: var(--paper); }
  .front-texture {
    position: absolute;
    inset: 0;
    background: linear-gradient(135deg, #fbfbfd 0%, #f1eff6 100%);
  }
  .front-stripe {
    position: absolute;
    inset: 0;
    background: var(--red);
    clip-path: polygon(58% 0, 100% 0, 100% 100%, 74% 100%);
  }
  .front-panel {
    position: absolute;
    inset: 0;
    background: linear-gradient(160deg, var(--navy-light) 0%, var(--navy) 55%, var(--navy-deep) 100%);
    clip-path: polygon(59.3% 0, 100% 0, 100% 100%, 75.3% 100%);
  }
  .identity {
    position: absolute;
    left: 40px;
    top: 70px;
    color: var(--ink);
  }
  .person-name {
    font-weight: 700;
    font-size: 29px;
    letter-spacing: 0.5px;
    line-height: 1.05;
    text-transform: uppercase;
  }
  .person-role {
    font-weight: 300;
    font-size: 23px;
    line-height: 1.2;
  }
  .contact-list {
    list-style: none;
    margin-top: 16px;
  }
  .contact-item {
    display: flex;
    align-items: center;
    gap: 12px;
    font-size: 14.5px;
    font-weight: 400;
    line-height: 1;
    margin-bottom: 11px;
    color: var(--ink);
  }
  .contact-icon {
    width: 24px;
    height: 24px;
    flex: none;
  }
  .brand-mark {
    position: absolute;
    display: flex;
    flex-direction: column;
    align-items: center;
    gap: 8px;
    color: var(--white);
    font-weight: 700;
    text-transform: uppercase;
    text-align: center;
  }
  .brand-dot {
    border-radius: 50%;
    background: var(--red);
  }
  .card-front .brand-mark {
    left: 345px;
    top: 92px;
    width: 180px;
    font-size: 22px;
    line-height: 1.05;
  }
  .card-front .brand-dot { width: 34px; height: 34px; }

  /* Back side */
  .card-back {
    background: var(--navy);
  }
  .back-texture {
    position: absolute;
    inset: 0;
    background: radial-gradient(ellipse at 50% 45%, var(--navy-light) 0%, var(--navy) 55%, var(--navy-deep) 100%);
  }
  .card-back .brand-mark {
    left: 0;
    right: 0;
    top: 100px;
    font-size: 36px;
    line-height: 1.05;
    gap: 12px;
  }
  .card-back .brand-dot { width: 44px; height: 44px; }
</style>
</head>
<body>
<main class="canvas">

  <section class="card card-front" aria-label="Business card front">
    <div class="front-texture" role="img" aria-label="Faint geometric star pattern on white"></div>
    <div class="front-stripe"></div>
    <div class="front-panel"></div>

    <div class="identity">
      <h1 class="person-name">Dora Quinlan</h1>
      <p class="person-role">Owner</p>
      <ul class="contact-list">
        <li class="contact-item">
          <svg class="contact-icon" viewBox="0 0 24 24" aria-hidden="true">
            <circle cx="12" cy="12" r="10.5" fill="none" stroke="#1b2d63" stroke-width="1.8"/>
            <path d="M9.2 7.5c-.6 0-1.4.8-1.4 1.9 0 2.9 3.6 6.9 6.6 6.9 1.1 0 1.8-.8 1.8-1.4l-1.7-1.2-1.1.8c-1-.4-2.4-1.8-2.8-2.8l.8-1.1z" fill="#1b2d63"/>
          </svg>
          (555) 314-2096
        </li>
        <li class="contact-item">
          <svg class="contact-icon" viewBox="0 0 24 24" aria-hidden="true">
            <circle cx="12" cy="12" r="10.5" fill="none" stroke="#1b2d63" stroke-width="1.8"/>
            <rect x="7" y="8.5" width="10" height="7" rx="1" fill="#1b2d63"/>
            <path d="M7.3 9l4.7 3.6L16.7 9" fill="none" stroke="#fff" stroke-width="1"/>
          </svg>
          Info@brightwellsnacks.example
        </li>
        <li class="contact-item">
          <svg class="contact-icon" viewBox="0 0 24 24" aria-hidden="true">
            <circle cx="12" cy="12" r="10.5" fill="none" stroke="#1b2d63" stroke-width="1.8"/>
            <path d="M8.5 8.5l7 2.6-2.9 1 -1 2.9z" fill="#1b2d63"/>
            <path d="M12.6 12.1l2.6 2.6" stroke="#1b2d63" stroke-width="1.4"/>
          </svg>
          Brightwellsnacks.example
        </li>
      </ul>
    </div>

    <div class="brand-mark">
      <span class="brand-dot" aria-hidden="true"></span>
      <span class="brand-name">Brightwell Snacks</span>
    </div>
  </section>

  <section class="card card-back" aria-label="Business card back">
    <div class="back-texture" role="img" aria-label="Tonal navy geometric star pattern"></div>
    <div class="brand-mark">
      <span class="brand-dot" aria-hidden="true"></span>
      <span class="brand-name">Brightwell<br>Snacks</span>
    </div>
  </section>

</main>
</body>
</html>
```